High-end law practice specializing in closely held business succession planning and complex estates

Solo practitioner whose practice specializes in high-net worth, complex estate planning needs muliple versions of letterhead black and white, please. Letterhead should incorporate slogan, "Protecting your family business is my business," for one and "Complex Estate Planning"; third with no slogan. All for The Law Office of Marguerite Elaine Haskett, PC, 418 Cedar Hollow Ln., Newport News, Virginia 23847, Tel. 757-481-5390 Fax tbd email: marguerite@mehcounsel.example; Marguerite Elaine Haskett, Esq., principal, licensed in VA, NY, DC
Updates

Project Deadline Extended
Reason: My internet service went down and I can only view designs on my smart phone -- it's just too hard to review. So sorry! Working with my ISP now. Please be patient!

Target Market(s)

High net worth clients with complex estate planning needs, family businesses, family farmers, family foresters -- people with unique estate/succession planning needs who need a specialist who understands them.

Industry/Entity Type

Business

Font styles to use
Script

Requirements
Must have
• A high-end look and feel, connoting trustworthiness, special knowledge, and expertise.

```html
<!DOCTYPE html>
<html lang="en">
<head>
<meta charset="utf-8">
<title>Letterhead – Marguerite Elaine Haskett, Esq.</title>
<link rel="stylesheet" href="https://fonts.googleapis.com/css2?family=Arimo:wght@400;700&family=Inter:wght@300&display=swap">
<style>
  :root {
    --band: #363435;
    --paper: #ffffff;
    --ink-light: #ffffff;
    --footer-ink: #555555;
    --icon-strip: #d9d9d9;
    --frame: #3a3a3a;
  }
  html, body { margin: 0; padding: 0; overflow: hidden; background: var(--paper); }
  .letterhead {
    position: relative;
    width: 849px;
    height: 1200px;
    box-sizing: border-box;
    border: 1px solid var(--frame);
    background: var(--paper);
    overflow: hidden;
    font-family: "Arimo", Arial, sans-serif;
  }
  .header-band {
    position: absolute;
    inset: 0 0 auto 0;
    height: 165px;
    background: var(--band);
  }
  .practice-tab {
    position: absolute;
    top: 0;
    left: 0;
    width: 849px;
    height: 96px;
  }
  .practice-icons {
    position: absolute;
    top: 30px;
    left: 388px;
    width: 420px;
    height: 44px;
    background: var(--icon-strip);
    border-radius: 4px;
  }
  .attorney {
    position: absolute;
    top: 52px;
    left: 43px;
    color: var(--ink-light);
    font-size: 26px;
    line-height: 33px;
  }
  .attorney-name { font-weight: 700; font-size: 24px; display: block; }
  .slogan {
    position: absolute;
    top: 98px;
    left: 518px;
    color: var(--ink-light);
    font-family: "Inter", Arial, sans-serif;
    font-weight: 300;
    font-size: 24.5px;
    line-height: 32px;
    letter-spacing: -0.2px;
  }
  .contact {
    position: absolute;
    left: 0;
    right: 0;
    bottom: 22px;
    text-align: center;
    color: var(--footer-ink);
    font-size: 16px;
    line-height: 30px;
  }
  .contact-line { display: flex; justify-content: center; align-items: center; gap: 14px; }
  .contact-item { display: inline-flex; align-items: center; gap: 6px; }
  .contact-item svg { width: 18px; height: 18px; stroke: var(--footer-ink); fill: none; stroke-width: 1.2; }
</style>
</head>
<body>
<div class="letterhead">
  <div class="header-band"></div>
  <svg class="practice-tab" viewBox="0 0 849 96" aria-hidden="true">
    <path d="M318 0 C338 0 345 10 348 30 L350 62 C352 84 364 96 392 96 L849 96 L849 0 Z" fill="#ffffff"/>
  </svg>
  <div class="practice-icons" role="img" aria-label="Row of line icons for legal practice areas: law book, justice, gavel, scales, calculator, family, passport, handshake"></div>

  <div class="attorney">
    <span class="attorney-name">Marguerite Elaine Haskett</span>
    Esq., principal,<br>
    licensed in VA, NY, DC
  </div>

  <div class="slogan">Protecting your family<br>business is my business.</div>

  <footer class="contact">
    <div class="contact-line">
      <span class="contact-item">
        <svg viewBox="0 0 18 18"><path d="M9 16 C5 11 4 9 4 7 A5 5 0 0 1 14 7 C14 9 13 11 9 16 Z"/><circle cx="9" cy="7" r="2"/></svg>
        PC, 418 Cedar Hollow Ln., Newport News, Virginia 23847,
      </span>
    </div>
    <div class="contact-line">
      <span class="contact-item">
        <svg viewBox="0 0 18 18"><path d="M2 7 C2 4 16 4 16 7 L13 8 L12 6 L6 6 L5 8 Z"/><path d="M5 9 L13 9 L15 14 L3 14 Z"/><circle cx="9" cy="11.5" r="1.3"/></svg>
        757-481-5390
      </span>
      <span class="contact-item">
        <svg viewBox="0 0 18 18"><rect x="5" y="2" width="8" height="5"/><rect x="2" y="7" width="14" height="6" rx="1"/><rect x="5" y="11" width="8" height="5"/></svg>
        757-555-018-2046
      </span>
      <span class="contact-item">
        <svg viewBox="0 0 18 18"><rect x="2" y="4" width="14" height="10"/><path d="M2 4 L9 10 L16 4"/></svg>
        marguerite@mehcounsel.example
      </span>
      <span class="contact-item">
        <svg viewBox="0 0 18 18"><circle cx="9" cy="9" r="7"/><ellipse cx="9" cy="9" rx="3" ry="7"/><path d="M2 9 H16 M3.5 5 H14.5 M3.5 13 H14.5"/></svg>
        www.mehcounsel.example
      </span>
    </div>
  </footer>
</div>
</body>
</html>
```